Physical Literacy company needs a web page designed...

We are a new company who provide physical education training to schools and deliver interventions to improve health and wellbeing, academic achievement through physical activity.

We need the website to have the following specification:
Creative design and production for 8 x page website for Kinetrova. Imagery and text as supplied by client. Fully responsive website design for multiple devices.
– 8 Main pages to website as per attached site plan – Twitter feed on home page
– Social Links - link to blog page
– Content management system for 2 pages
– Site Testing and Implementation
– Cookies policy and legal document templates if necessary

I am attaching a business plan PPT to give you a better idea of business. This should enable you to lift a lot of the content from the PPT also.

Target Market(s)

Physical Education - Schools
Families who wish to be more physically active

Industry/Entity Type

Education

Number of Pages Required

5+ page

Font styles to use
Sans Serif
Other font styles liked:
• Chalkboard

Colors
fbee3e
33a6d7
ec1f27
9bcb3c

Requirements
Must have
• *Home page
• *biog of company and four co-founders - who are well? What do we do? How do we do it? Contact details
• *Content management for two pages - blog page and case studies
• *Live twitter feed
• *links to youtube videos

```html
<!DOCTYPE html>
<html lang="en">
<head>
<meta charset="utf-8">
<title>Kinetrova — Physical Literacy for Schools and Families</title>
<link href="https://fonts.googleapis.com/css2?family=Dosis:wght@400;500;600;700&display=swap" rel="stylesheet">
<style>
:root{
  --purple:#8a6fd6;
  --purple-dark:#7a62c9;
  --orange:#f8b03c;
  --pink:#ef6f6a;
  --green:#92c154;
  --blue:#5ec6dc;
  --magenta:#c463cf;
  --rose:#e46fb5;
  --text:#666;
  --line:#eee;
}
*{margin:0;padding:0;box-sizing:border-box}
html,body{width:1200px;height:3232px;overflow:hidden}
body{font-family:'Dosis',sans-serif;color:var(--text);background:#fff;position:relative}
.abs{position:absolute}

/* header */
.colour-bars{left:625px;top:0;width:517px;height:7px;display:flex}
.colour-bars span{flex:1}
.brand{left:86px;top:30px;font-size:34px;font-weight:700;color:var(--orange);letter-spacing:1px;display:flex;align-items:center;gap:10px}
.brand i{width:14px;height:14px;border-radius:50%;background:var(--orange);display:block}
.nav-item{top:25px;width:120px;margin-left:-60px;text-align:center;font-size:14px;color:var(--purple-dark)}
.nav-item .dot{width:43px;height:43px;border-radius:50%;margin:0 auto 12px;display:flex;align-items:center;justify-content:center}
.nav-sep{top:85px;width:2px;height:12px;background:var(--orange)}

/* hero */
.hero{left:0;top:108px;width:1200px;height:448px;background:linear-gradient(100deg,#e9b58d 0%,#f3c9a6 20%,#f1d7c4 40%,#fbfaf8 62%,#fff 100%)}
.hero-badge{left:930px;top:478px;width:190px;height:44px;background:var(--orange);border-radius:4px;color:#fff;font-size:24px;font-weight:700;letter-spacing:1px;display:flex;align-items:center;justify-content:center}

/* welcome */
.section-title{font-size:30px;font-weight:600}
.welcome-title{left:95px;top:582px;color:var(--orange)}
.welcome-text{left:95px;top:636px;width:555px;font-size:13.5px;line-height:24px}
.ticks{left:95px;top:728px;list-style:none;font-size:13.5px;line-height:27px}
.ticks li{display:flex;align-items:center;gap:12px}
.btn{left:95px;top:836px;width:119px;height:39px;border-radius:8px;background:var(--orange);color:#fff;font-weight:600;font-size:13px;display:flex;align-items:center;justify-content:center;box-shadow:0 3px 0 #e39a2a}
.welcome-photo{left:685px;top:646px;width:403px;height:226px;border-radius:6px;background:radial-gradient(ellipse at 50% 60%,#f2c4c2 0%,#e7b6d7 35%,#f4eef2 70%,#fff 100%)}

/* stats */
.stats{left:0;top:958px;width:1200px;height:212px;background:var(--purple)}
.stat{top:1012px;width:237px;height:102px;border-radius:8px;background:rgba(255,255,255,.1);border:1px solid rgba(255,255,255,.18);display:flex;align-items:center;gap:16px;padding-left:20px;color:#fff}
.stat .ic{width:54px;height:54px;border-radius:50%;background:rgba(255,255,255,.22);display:flex;align-items:center;justify-content:center}
.stat b{display:block;font-size:30px;font-weight:500;line-height:32px}
.stat small{font-size:11px}

/* headings */
.center-title{left:0;width:1200px;text-align:center}
.deco{left:520px;width:160px;height:14px}
.intro{left:335px;top:1312px;width:530px;text-align:center;font-size:13.5px;line-height:24px}

/* classes */
.card{top:1422px;width:314px;height:474px;border-radius:14px;overflow:hidden;background:#fff;box-shadow:0 0 0 1px var(--line)}
.card .img{height:248px}
.card .body{padding:20px 24px 0;position:relative;height:178px}
.card h3{font-size:21px;font-weight:600;color:var(--purple-dark)}
.card .time{font-size:11.5px;margin-top:4px}
.card .price{position:absolute;right:24px;top:18px;text-align:right;color:var(--orange);font-size:22px;font-weight:600;line-height:24px}
.card .price small{display:block;font-size:11px;color:var(--text);font-weight:400}
.card .dots{width:30px;border-top:2px dotted #ccc;margin:12px 0 18px}
.card p{font-size:13.5px;line-height:22px}
.card .bar{display:flex;height:48px;color:#fff;font-size:11.5px;font-weight:700}
.bar .age{background:var(--green);width:128px;display:flex;align-items:center;justify-content:center}
.bar .size{background:var(--pink);flex:1;display:flex;align-items:center;justify-content:center}
.bar .go{background:var(--orange);width:45px;display:flex;align-items:center;justify-content:center;font-size:18px}

.divider{left:10px;width:1180px;border-top:2px dashed var(--orange)}
.divider-star{left:592px;width:16px;height:16px}

/* services */
.svc{width:300px}
.svc .ic{position:absolute;top:0;width:68px;height:68px;border-radius:50%;display:flex;align-items:center;justify-content:center;border:4px solid #fff;box-shadow:0 0 0 2px currentColor}
.svc h4{font-size:24px;font-weight:600;margin-bottom:14px;line-height:28px}
.svc p{font-size:13.5px;line-height:22px;color:var(--text)}
.svc.left{padding-left:90px}
.svc.left .ic{left:2px}
.svc.right{padding-right:90px;text-align:right}
.svc.right .ic{right:2px}
.svc.right p{text-align:left}
.svc-art{left:442px;top:2232px;width:312px;height:375px;border-radius:10px;background:radial-gradient(ellipse at 50% 70%,#f6c28d 0%,#f4d3ba 30%,#e8f3fa 62%,#fff 100%)}

/* news */
.news-img{top:2876px;width:198px;height:150px;border-radius:10px}
.news-date{width:88px;height:28px;margin-left:-44px;background:var(--green);color:#fff;font-size:11px;font-weight:600;border-radius:4px;display:flex;align-items:center;justify-content:center}
.news h3{font-size:24px;font-weight:600;line-height:29px;color:var(--purple-dark)}
.news .meta{font-size:11.5px;margin:8px 0}
.news .dots{width:30px;border-top:2px dotted #ccc;margin-bottom:10px}
.news p{font-size:13.5px;line-height:22px;width:270px}
.news a{display:block;font-size:13px;color:var(--orange);margin-top:10px;text-decoration:none}

/* footer */
.footer{left:0;top:3130px;width:1200px;height:102px;background:var(--purple-dark)}
.f-col{top:3162px;width:240px;margin-left:-120px;text-align:center;color:#fff;font-size:13px;line-height:22px}
.f-hex{top:3110px;width:38px;height:42px;margin-left:-19px}
.social{left:875px;top:3166px;width:210px;display:flex;flex-wrap:wrap;gap:10px 18px;justify-content:center}
.social span{width:13px;height:13px;border-radius:50%;background:#fff;display:block}
</style>
</head>
<body>

<header>
<div class="abs colour-bars"><span style="background:var(--purple)"></span><span style="background:var(--orange)"></span><span style="background:var(--pink)"></span><span style="background:var(--green)"></span><span style="background:var(--blue)"></span></div>
<div class="abs brand"><i></i>KINETROVA</div>

<div class="abs nav-item" style="left:672px"><div class="dot" style="background:var(--purple)"><svg width="18" height="18" viewBox="0 0 18 18"><path d="M9 2 1 9h2v7h4v-5h4v5h4V9h2z" fill="#fff"/></svg></div>Home</div>
<div class="abs nav-sep" style="left:716px"></div>
<div class="abs nav-item" style="left:765px"><div class="dot" style="background:var(--orange)"><svg width="18" height="18" viewBox="0 0 18 18"><circle cx="9" cy="9" r="7" fill="none" stroke="#fff" stroke-width="2"/><path d="M5.5 10.5q3.5 3.5 7 0" fill="none" stroke="#fff" stroke-width="1.8"/></svg></div>About Us</div>
<div class="abs nav-sep" style="left:810px"></div>
<div class="abs nav-item" style="left:862px"><div class="dot" style="background:var(--pink)"><svg width="18" height="18" viewBox="0 0 18 18"><rect x="2" y="3" width="12" height="13" rx="2" fill="none" stroke="#fff" stroke-width="2"/><path d="M8 11 16 3" stroke="#fff" stroke-width="2"/></svg></div>Our Packages</div>
<div class="abs nav-sep" style="left:912px"></div>
<div class="abs nav-item" style="left:961px"><div class="dot" style="background:var(--green)"><svg width="18" height="18" viewBox="0 0 18 18"><rect x="2" y="3" width="14" height="12" rx="2" fill="none" stroke="#fff" stroke-width="2"/><path d="M4 13l4-4 3 3 2-2 2 3z" fill="#fff"/></svg></div>Case Studies</div>
<div class="abs nav-sep" style="left:1010px"></div>
<div class="abs nav-item" style="left:1058px"><div class="dot" style="background:var(--blue)"><svg width="18" height="18" viewBox="0 0 18 18"><path d="M3 15 14 4l1.5 1.5L4.5 16.5H3z" fill="#fff"/></svg></div>Contact Us</div>
<div class="abs nav-sep" style="left:1103px"></div>
</header>

<div class="abs hero" role="img" aria-label="Child holding up paint-covered hands beside colourful alphabet letters"></div>
<div class="abs hero-badge">KINETROVA</div>

<section>
<h2 class="abs section-title welcome-title">Welcome</h2>
<p class="abs welcome-text">Kinetrova is a new physical literacy company founded by four co-founders with a shared aim: to train schools in physical education and deliver interventions that lift health, wellbeing and academic achievement through physical activity.</p>
<ul class="abs ticks">
  <li><svg width="12" height="10" viewBox="0 0 12 10"><path d="M1 5l3.5 3.5L11 1" fill="none" stroke="#555" stroke-width="2"/></svg>Who we are: four co-founders from teaching, coaching and health</li>
  <li><svg width="12" height="10" viewBox="0 0 12 10"><path d="M1 5l3.5 3.5L11 1" fill="none" stroke="#555" stroke-width="2"/></svg>What we do: PE training for schools and active family sessions</li>
  <li><svg width="12" height="10" viewBox="0 0 12 10"><path d="M1 5l3.5 3.5L11 1" fill="none" stroke="#555" stroke-width="2"/></svg>How we do it: fun, measured movement that helps children learn</li>
</ul>
<div class="abs btn">Read more</div>
<div class="abs welcome-photo" role="img" aria-label="Parents and young children playing active games together"></div>
</section>

<section>
<div class="abs stats"></div>
<div class="abs stat" style="left:112px"><div class="ic"><svg width="26" height="20" viewBox="0 0 26 20"><path d="M13 1 1 7l12 6 12-6zM6 10v5q7 5 14 0v-5l-7 3.5z" fill="#fff"/></svg></div><div><b>2695</b><small>New Students</small></div></div>
<div class="abs stat" style="left:357px"><div class="ic"><svg width="22" height="22" viewBox="0 0 22 22"><path d="M5 2h12v5a6 6 0 0 1-12 0zM2 3h3v3q-3 0-3-3zM17 3h3q0 3-3 3zM9 13h4v4h3v3H6v-3h3z" fill="#fff"/></svg></div><div><b>4568</b><small>Gold Medals</small></div></div>
<div class="abs stat" style="left:602px"><div class="ic"><svg width="20" height="22" viewBox="0 0 20 22"><path d="M3 2h13v16H5a2 2 0 0 0 0 3h12" fill="#fff" stroke="#fff" stroke-width="1.5"/></svg></div><div><b>8685</b><small>Total Courses</small></div></div>
<div class="abs stat" style="left:847px"><div class="ic"><svg width="20" height="22" viewBox="0 0 20 22"><path d="M7 1h6M8 1v7L2 19q-1 2 1 2h14q2 0 1-2L12 8V1" fill="#fff"/></svg></div><div><b>7856</b><small>Total Activities</small></div></div>
</section>

<section>
<h2 class="abs section-title center-title" style="top:1225px;color:var(--purple-dark)">Our Classes</h2>
<svg class="abs deco" style="top:1277px" viewBox="0 0 160 14"><path d="M8 5h62M8 9h62M90 5h62M90 9h62" stroke="var(--orange)" stroke-width="1.5"/><path d="M74 11l12-8-4 10z" fill="var(--purple)"/></svg>
<p class="abs intro">Our classes build physical literacy: the confidence, skill and motivation to move for life. Each session mixes play with learning so children grow stronger, calmer and more ready to learn in class, and families can join in at home.</p>

<div class="abs card" style="left:95px">
  <div class="img" role="img" aria-label="Children practising balance and movement in a classroom" style="background:linear-gradient(135deg,#f4f0e8,#c9d97a 55%,#7aa4c8)"></div>
  <div class="body"><h3>Agility Match</h3><div class="time">&#9719; 9:00 am - 11:00 am</div><div class="price">$25<small>per day</small></div><div class="dots"></div><p>Quick feet, changes of direction and games that sharpen focus.</p></div>
  <div class="bar"><div class="age">AGE: 2-5 YEARS</div><div class="size">CLASS SIZE: 25</div><div class="go">&#8250;</div></div>
</div>
<div class="abs card" style="left:444px">
  <div class="img" role="img" aria-label="Parent and child doing an activity together outdoors" style="background:linear-gradient(135deg,#c8df7c,#f1cfa8 50%,#9fc95a)"></div>
  <div class="body"><h3>Balance Play</h3><div class="time">&#9719; 10:00 am - 1:00 pm</div><div class="price">$35<small>per day</small></div><div class="dots"></div><p>Steady, controlled movement that builds core strength and calm.</p></div>
  <div class="bar"><div class="age">AGE: 2-5 YEARS</div><div class="size">CLASS SIZE: 30</div><div class="go">&#8250;</div></div>
</div>
<div class="abs card" style="left:790px">
  <div class="img" role="img" aria-label="Child climbing over large soft play blocks" style="background:linear-gradient(135deg,#9a3a4a,#e3a05a 50%,#d8c244)"></div>
  <div class="body"><h3>Ball Skills</h3><div class="time">&#9719; 9:30 am - 12:00 am</div><div class="price">$45<small>per day</small></div><div class="dots"></div><p>Throwing, catching and kicking games that grow coordination.</p></div>
  <div class="bar"><div class="age">AGE: 2-5 YEARS</div><div class="size">CLASS SIZE: 35</div><div class="go">&#8250;</div></div>
</div>
</section>

<div class="abs divider" style="top:1982px"></div>
<svg class="abs divider-star" style="top:1975px" viewBox="0 0 16 16"><path d="M8 1l2 5h5l-4 3 2 6-5-4-5 4 2-6-4-3h5z" fill="var(--purple)"/></svg>

<section>
<h2 class="abs section-title center-title" style="top:2065px;color:var(--purple-dark)">Our Services</h2>
<svg class="abs deco" style="top:2117px" viewBox="0 0 160 14"><path d="M8 5h62M8 9h62M90 5h62M90 9h62" stroke="var(--orange)" stroke-width="1.5"/><path d="M73 4h14l-7 8z" fill="var(--purple)"/></svg>

<div class="abs svc left" style="left:95px;top:2194px;color:var(--magenta)"><div class="ic" style="background:var(--magenta)"><svg width="24" height="24" viewBox="0 0 24 24"><path d="M6 2v8M4 2v6a2 2 0 0 0 4 0V2M6 10v12M17 2q-3 3-3 9h3v11" fill="none" stroke="#fff" stroke-width="2"/></svg></div><h4>Healthy Habits</h4><p>Simple food and sleep routines that give children energy to move, play and learn.</p></div>
<div class="abs svc left" style="left:95px;top:2356px;color:var(--green)"><div class="ic" style="background:var(--green)"><svg width="24" height="24" viewBox="0 0 24 24"><path d="M5 22V3M5 4h13l-3 4 3 4H5" fill="none" stroke="#fff" stroke-width="2"/></svg></div><h4>Active Lessons</h4><p>Movement breaks built into maths and reading to lift focus and results.</p></div>
<div class="abs svc left" style="left:95px;top:2518px;color:var(--orange)"><div class="ic" style="background:var(--orange)"><svg width="24" height="24" viewBox="0 0 24 24"><rect x="4" y="3" width="16" height="16" rx="3" fill="none" stroke="#fff" stroke-width="2"/><path d="M4 11h16M8 19v2M16 19v2" stroke="#fff" stroke-width="2"/></svg></div><h4>School Visits</h4><p>Our coaches come to you, with kit, plans and staff PE training on site.</p></div>

<div class="abs svc-art" role="img" aria-label="Children playing active games under kites and paper planes"></div>

<div class="abs svc right" style="left:803px;top:2194px;color:var(--pink)"><div class="ic" style="background:var(--pink)"><svg width="24" height="24" viewBox="0 0 24 24"><rect x="3" y="5" width="18" height="16" rx="2" fill="none" stroke="#fff" stroke-width="2"/><path d="M3 10h18M8 3v4M16 3v4M9 15l2 2 4-4" fill="none" stroke="#fff" stroke-width="2"/></svg></div><h4>Full Day Session</h4><p>A whole day of PE, active learning and play for a class or year group.</p></div>
<div class="abs svc right" style="left:803px;top:2356px;color:var(--purple-dark)"><div class="ic" style="background:var(--purple)"><svg width="24" height="24" viewBox="0 0 22 22"><path d="M5 2h12v5a6 6 0 0 1-12 0zM2 3h3v3q-3 0-3-3zM17 3h3q0 3-3 3zM9 13h4v4h3v3H6v-3h3z" fill="#fff"/></svg></div><h4>Family Sessions</h4><p>Weekend sessions for families who want to be more active together.</p></div>
<div class="abs svc right" style="left:803px;top:2518px;color:var(--blue)"><div class="ic" style="background:var(--blue)"><svg width="26" height="20" viewBox="0 0 26 20"><path d="M13 1 1 7l12 6 12-6zM6 10v5q7 5 14 0v-5l-7 3.5z" fill="#fff"/></svg></div><h4>Qualified Coaches</h4><p>Trained PE teachers and coaches who track each child's progress.</p></div>
</section>

<div class="abs divider" style="top:2699px;border-color:var(--purple)"></div>
<svg class="abs divider-star" style="top:2692px" viewBox="0 0 16 16"><path d="M8 1l2 5h5l-4 3 2 6-5-4-5 4 2-6-4-3h5z" fill="var(--purple)"/></svg>

<section>
<h2 class="abs section-title center-title" style="top:2757px;color:var(--rose)">Latest News</h2>
<svg class="abs deco" style="top:2809px" viewBox="0 0 160 14"><path d="M8 5h62M8 9h62M90 5h62M90 9h62" stroke="var(--green)" stroke-width="1.5"/><path d="M74 5h4l6-3v10l-6-3h-4z" fill="var(--rose)"/></svg>

<div class="abs news-img" style="left:95px;background:linear-gradient(135deg,#f2b24a,#e06a8a 50%,#9ccb62)" role="img" aria-label="Children smiling on a colourful playground"></div>
<div class="abs news-date" style="left:194px;top:3012px">FEB 4, 2016</div>
<div class="abs news" style="left:317px;top:2872px"><h3>Make Learning Fun for<br>Your Kids</h3><div class="meta">&#9679; Amy Hart &nbsp;&nbsp; &#9993; 4 Comments</div><div class="dots"></div><p>Watch our new video series on active lessons you can try in class today.</p><a>Read more &raquo;</a></div>

<div class="abs news-img" style="left:616px;background:linear-gradient(135deg,#5c8a3a,#a5cf6a 50%,#e9e4d8)" role="img" aria-label="Schoolchildren standing together outdoors after school"></div>
<div class="abs news-date" style="left:715px;top:3012px">JAN 24, 2016</div>
<div class="abs news" style="left:838px;top:2872px"><h3>After School Activities<br>for Kids</h3><div class="meta">&#9679; Amy Hart &nbsp;&nbsp; &#9993; 0 Comments</div><div class="dots"></div><p>Ideas from our case studies to keep the whole family moving after school.</p><a>Read more &raquo;</a></div>
</section>

<footer>
<div class="abs footer"></div>
<svg class="abs f-hex" style="left:222px" viewBox="0 0 38 42"><path d="M19 1l17 10v20L19 41 2 31V11z" fill="var(--green)"/><path d="M19 12a6 6 0 0 0-6 6c0 5 6 11 6 11s6-6 6-11a6 6 0 0 0-6-6zm0 8a2 2 0 1 1 0-4 2 2 0 0 1 0 4z" fill="#fff"/></svg>
<svg class="abs f-hex" style="left:474px" viewBox="0 0 38 42"><path d="M19 1l17 10v20L19 41 2 31V11z" fill="var(--pink)"/><path d="M13 13l4-1 2 5-2 2q2 4 5 5l2-2 5 2-1 4q-10 0-15-15z" fill="#fff"/></svg>
<svg class="abs f-hex" style="left:728px" viewBox="0 0 38 42"><path d="M19 1l17 10v20L19 41 2 31V11z" fill="var(--orange)"/><rect x="11" y="14" width="16" height="12" rx="1" fill="#fff"/><path d="M11 15l8 6 8-6" fill="none" stroke="var(--orange)" stroke-width="1.5"/></svg>
<svg class="abs f-hex" style="left:980px" viewBox="0 0 38 42"><path d="M19 1l17 10v20L19 41 2 31V11z" fill="var(--green)"/><path d="M12 19h4v9h-4zM17 19l3-6q2 0 2 2l-1 4h5q1 1 0 2l-2 7h-7z" fill="#fff"/></svg>

<div class="abs f-col" style="left:222px">456 Orchard Lane,<br>Leeds 1234.</div>
<div class="abs f-col" style="left:474px">+1 (555) 010-4567<br>+1 (555) 010-4567</div>
<div class="abs f-col" style="left:728px">info@kinetrova.example<br>support@kinetrova.example</div>
<div class="abs social" role="list" aria-label="Social links: live feed, video channel and blog">
  <span role="listitem" aria-label="Live feed"></span><span role="listitem" aria-label="Community page"></span><span role="listitem" aria-label="Photo board"></span><span role="listitem" aria-label="Video channel"></span><span role="listitem" aria-label="Photo stream"></span><span role="listitem" aria-label="Blog feed"></span><span role="listitem" aria-label="Professional network"></span><span role="listitem" aria-label="Email updates"></span><span role="listitem" aria-label="Profile page"></span><span role="listitem" aria-label="Gallery"></span>
</div>
</footer>

</body>
</html>
```